TRENDY & MODERN BUSINESS CARD DESIGN for Media Company *

I need a minimalistic - clean - modern and professional business card layout and design for MEDIA & PHOTOGRAPHY STUDIO.

We do NOT have a logo, and not really looking for one - but rather excellent typography and design. We would consider the 3 as a focal point.

We do personal and commercial photography.

Target Market(s)

Personal and commercial photography clientele

Contact Information for Business Card

ZUB size - from zub.com / size guidelines are enclosed in the brief

Font styles to use
Sans Serif

Colors
f78f20
eda3c7
cee9f5
0555a3
e667a6
fbf289

Requirements
Must have
• Clean lines - Modern layout
Nice to have
• All blue background as an option - use color palette in brief please.
Should not have
• Old fashion fonts and regular fonts.

```html
<!DOCTYPE html>
<html lang="en">
<head>
<meta charset="utf-8">
<title>Nova Frame Media – Business Card</title>
<link rel="stylesheet" href="https://fonts.googleapis.com/css2?family=Exo+2:wght@600;700;800&display=swap">
<style>
  :root {
    --bg: #e5e5e5;
    --brand-blue: #0555a3;
    --accent-orange: #f78f20;
    --card-white: #f8f8f8;
    --ink: #1b1b1b;
    --white: #ffffff;
  }
  * { box-sizing: border-box; margin: 0; padding: 0; }
  html, body {
    width: 1200px; height: 1200px; overflow: hidden;
    background: var(--bg);
    font-family: "Exo 2", Arial, sans-serif;
  }
  .canvas { position: relative; width: 1200px; height: 1200px; }

  .card {
    position: absolute; left: 291px; width: 632px; height: 424px;
    box-shadow: 0 10px 22px rgba(0,0,0,0.18);
    overflow: visible;
  }

  /* Front */
  .card-front { top: 126px; background: var(--brand-blue); }
  .front-brand {
    position: absolute; left: 0; right: 0; top: 178px;
    text-align: center; color: var(--white);
  }
  .brand-name {
    font-weight: 800; font-size: 40px; letter-spacing: 1px; line-height: 1;
    text-transform: uppercase;
  }
  .brand-tagline {
    margin-top: 12px; font-weight: 700; font-size: 27px; line-height: 1;
  }

  /* Back */
  .card-back { top: 637px; background: var(--card-white); }
  .back-panel {
    position: absolute; left: 0; top: 0; width: 184px; height: 100%;
    background: var(--brand-blue);
  }
  .panel-name {
    position: absolute; left: 92px; top: 212px;
    transform: translate(-50%, -50%) rotate(-90deg);
    white-space: nowrap; color: var(--white);
    font-weight: 800; font-size: 36px; letter-spacing: 1px; text-transform: uppercase;
  }

  .person { position: absolute; left: 184px; right: 0; top: 62px; text-align: center; }
  .person-name { font-weight: 800; font-size: 38px; color: var(--ink); line-height: 1; }
  .person-name .surname { color: var(--accent-orange); }
  .person-role { margin-top: 6px; font-weight: 700; font-size: 13px; color: var(--ink); }

  .contact-row { position: absolute; left: 174px; height: 52px; display: flex; align-items: center; }
  .contact-tab {
    width: 50px; height: 52px; background: var(--accent-orange);
    border-radius: 0 26px 26px 0;
    display: flex; align-items: center; justify-content: center;
  }
  .contact-tab svg { width: 24px; height: 24px; }
  .contact-text { margin-left: 20px; color: var(--ink); font-weight: 700; }
  .contact-text.large { font-size: 25px; }
  .contact-text.small { font-size: 13.5px; line-height: 1.35; }
  .row-email { top: 186px; }
  .row-phone { top: 258px; }
  .row-address { top: 330px; }
</style>
</head>
<body>
<main class="canvas">

  <section class="card card-front">
    <div class="front-brand">
      <div class="brand-name">Nova Frame Media</div>
      <div class="brand-tagline">Capturing Life. Creating Art.</div>
    </div>
  </section>

  <section class="card card-back">
    <div class="back-panel">
      <div class="panel-name">Nova Frame Media</div>
    </div>

    <div class="person">
      <div class="person-name">Marisol <span class="surname">Vega</span></div>
      <div class="person-role">Founder &amp; Media Director</div>
    </div>

    <div class="contact-row row-email">
      <div class="contact-tab">
        <svg viewBox="0 0 24 24" fill="none" stroke="#fff" stroke-width="2" stroke-linejoin="round">
          <path d="M3 10 L12 4 L21 10 V20 H3 Z"/>
          <path d="M3 10 L12 16 L21 10"/>
        </svg>
      </div>
      <div class="contact-text large">mari@novaframemedia.com</div>
    </div>

    <div class="contact-row row-phone">
      <div class="contact-tab">
        <svg viewBox="0 0 24 24" fill="#fff">
          <path d="M6.6 10.8a15.1 15.1 0 0 0 6.6 6.6l2.2-2.2c.3-.3.7-.4 1-.2 1.1.4 2.3.6 3.6.6.6 0 1 .4 1 1V20c0 .6-.4 1-1 1C10.6 21 3 13.4 3 4c0-.6.4-1 1-1h3.5c.6 0 1 .4 1 1 0 1.3.2 2.5.6 3.6.1.3 0 .7-.2 1z"/>
        </svg>
      </div>
      <div class="contact-text large">(305) 555-0148</div>
    </div>

    <div class="contact-row row-address">
      <div class="contact-tab">
        <svg viewBox="0 0 24 24" fill="#fff">
          <path d="M12 2a7 7 0 0 0-7 7c0 5.2 7 13 7 13s7-7.8 7-13a7 7 0 0 0-7-7zm0 9.5A2.5 2.5 0 1 1 12 6.5a2.5 2.5 0 0 1 0 5z"/>
        </svg>
      </div>
      <div class="contact-text small">2400 Harbor Avenue, 9 th Floor<br>Miami, FL 33130</div>
    </div>
  </section>

</main>
</body>
</html>
```